Bright Harbor Construction

We are a commercial construction company specializing in steel stud framing, drywall, taping and acoustical ceilings. We would like a company logo (Something that looks great and isnt boring) as we have not been able to come up with one. A modern looking card would definitely suit our personalities best

We would like to try and avoid using dark colors. I have learned from experience that dark colors are the last to looked at. Thank you

```html
<!DOCTYPE html>
<html lang="en">
<head>
<meta charset="utf-8">
<title>Bright Harbor Construction – Business Card</title>
<link rel="stylesheet" href="https://fonts.googleapis.com/css2?family=Poppins:wght@600&family=Roboto:wght@400;700&display=swap">
<style>
  :root {
    --backdrop: #4b4b4d;
    --card-front: #eef6fb;
    --card-light: #ffffff;
    --panel: #3ea8d6;
    --accent: #4ab3d8;
    --accent-deep: #2a85b8;
    --mark-light: #6cc6e2;
    --text-light: #ffffff;
    --text-slate: #34485c;
  }
  * { box-sizing: border-box; margin: 0; padding: 0; }
  html, body {
    width: 1200px; height: 1139px; overflow: hidden;
    background: var(--backdrop);
  }
  .canvas { position: relative; width: 1200px; height: 1139px; }
  .card {
    position: absolute; left: 240px; width: 692px; height: 408px;
    border-radius: 38px; overflow: hidden;
    box-shadow: 0 14px 30px rgba(0,0,0,0.35);
  }
  .card-front { top: 124px; background: var(--card-front); }
  .card-back { top: 603px; background: var(--card-light); }

  .brand {
    position: absolute; display: flex; flex-direction: column; align-items: center;
    font-family: 'Poppins', sans-serif; font-weight: 600; color: var(--text-slate);
    text-align: center; white-space: nowrap;
  }
  .brand-mark { display: block; background: var(--accent); }
  .brand-name { display: block; line-height: 1; }
  .brand-sub { display: block; text-transform: uppercase; line-height: 1; }

  .card-front .brand { left: 0; right: 0; top: 66px; }
  .card-front .brand-mark { width: 118px; height: 118px; margin-bottom: 34px; }
  .card-front .brand-name { font-size: 40px; }
  .card-front .brand-sub { font-size: 16px; letter-spacing: 2px; margin-top: 14px; }
  .front-tab {
    position: absolute; left: 157px; bottom: 0; width: 372px; height: 31px;
    background: var(--accent); border-radius: 28px 28px 0 0;
  }

  .back-panel {
    position: absolute; left: 0; top: 0; width: 352px; height: 100%;
    background: var(--panel);
  }
  .back-tab {
    position: absolute; left: 0; top: 79px; width: 30px; height: 251px;
    background: var(--accent-deep); border-radius: 0 20px 20px 0;
  }
  .holder {
    position: absolute; left: 83px; top: 97px; color: var(--text-light);
    font-family: 'Roboto', sans-serif;
  }
  .holder-name { font-size: 25px; font-weight: 700; letter-spacing: -0.2px; line-height: 1; }
  .holder-role { font-size: 16px; margin-top: 9px; line-height: 1; }
  .contacts {
    position: absolute; left: 91px; top: 179px; list-style: none;
    font-family: 'Roboto', sans-serif; font-size: 16.5px; color: var(--text-light);
  }
  .contacts li { display: flex; align-items: center; height: 33px; }
  .contacts svg { width: 17px; height: 17px; margin-right: 12px; fill: var(--text-light); flex: none; }

  .card-back .brand { left: 352px; right: 0; top: 88px; }
  .card-back .brand-mark { width: 100px; height: 100px; margin-bottom: 42px; }
  .card-back .brand-name { font-size: 32px; }
  .card-back .brand-sub { font-size: 14px; letter-spacing: 1.6px; margin-top: 12px; }
</style>
</head>
<body>
<main class="canvas">
  <section class="card card-front">
    <div class="brand">
      <span class="brand-mark"></span>
      <span class="brand-name">Bright Harbor</span>
      <span class="brand-sub">Construction</span>
    </div>
    <span class="front-tab"></span>
  </section>

  <section class="card card-back">
    <div class="back-panel">
      <span class="back-tab"></span>
      <div class="holder">
        <p class="holder-name">YOR NAME HERE</p>
        <p class="holder-role">Designation</p>
      </div>
      <ul class="contacts">
        <li><svg viewBox="0 0 24 24"><path d="M6.6 10.8a15.1 15.1 0 0 0 6.6 6.6l2.2-2.2c.3-.3.7-.4 1-.2 1.1.4 2.3.6 3.6.6.6 0 1 .4 1 1V20c0 .6-.4 1-1 1A17 17 0 0 1 3 4c0-.6.4-1 1-1h3.5c.6 0 1 .4 1 1 0 1.3.2 2.5.6 3.6.1.3 0 .7-.2 1z"/></svg>XXX-XXX-XXXX</li>
        <li><svg viewBox="0 0 24 24"><path d="M2 5h20v2l-10 6L2 7zM2 9l10 6 10-6v10H2z"/></svg>name@brightharbor.com</li>
        <li><svg viewBox="0 0 24 24"><path d="M12 2a10 10 0 1 0 0 20 10 10 0 0 0 0-20zm6.9 6h-3a15 15 0 0 0-1.3-3.9A8 8 0 0 1 18.9 8zM12 4c.8 1.2 1.5 2.5 1.9 4h-3.8c.4-1.5 1.1-2.8 1.9-4zM4.3 14a8 8 0 0 1 0-4h3.4a16 16 0 0 0 0 4zm.8 2h3a15 15 0 0 0 1.3 3.9A8 8 0 0 1 5.1 16zm3-8h-3a8 8 0 0 1 4.3-3.9A15 15 0 0 0 8.1 8zM12 20c-.8-1.2-1.5-2.5-1.9-4h3.8c-.4 1.5-1.1 2.8-1.9 4zm2.3-6H9.7a14 14 0 0 1 0-4h4.6a14 14 0 0 1 0 4zm.3 5.9a15 15 0 0 0 1.3-3.9h3a8 8 0 0 1-4.3 3.9zm1.7-5.9a16 16 0 0 0 0-4h3.4a8 8 0 0 1 0 4z"/></svg>brightharbor.com</li>
        <li><svg viewBox="0 0 24 24"><path d="M12 2a7 7 0 0 0-7 7c0 5.2 7 13 7 13s7-7.8 7-13a7 7 0 0 0-7-7zm0 9.5a2.5 2.5 0 1 1 0-5 2.5 2.5 0 0 1 0 5z"/></svg>Your adress here</li>
      </ul>
    </div>
    <div class="brand">
      <span class="brand-mark"></span>
      <span class="brand-name">Bright Harbor</span>
      <span class="brand-sub">Construction</span>
    </div>
  </section>
</main>
</body>
</html>
```